TwirlPopix Balloon Logo and Product Packaging Design

I need a package design for twisting balloons for my website twirlpopics.com. The brand name that we will use is "twirlpopix". The packaging will be 40cm long x 15 cm width with a see thru front and a top that can tear off. We can only use 3 colors max, but two colors would be better. We also will need a logo for "twirlpopix". I have included our mockup front and back, our competitors packaging and our style guide. You can use our style guide and our mockups for inspiration but you please don't follow it exactly. You can also ignore them all together. Thanks, Dorian

```html
<!DOCTYPE html>
<html lang="en">
<head>
<meta charset="utf-8">
<title>TwirlPopix – Balloon Packaging</title>
<link href="https://fonts.googleapis.com/css2?family=Encode+Sans+Semi+Condensed:wght@400;500;600&family=Ubuntu:wght@400;500&display=swap" rel="stylesheet">
<style>
  :root{
    --slate:#475254;
    --slate-light:#5a6567;
    --red:#f5130f;
    --red-soft:#ff4a3a;
    --pink:#fbd3d3;
    --sky:#bdeef7;
    --white:#ffffff;
  }
  *{margin:0;padding:0;box-sizing:border-box}
  html,body{width:848px;height:1200px;overflow:hidden;background:var(--slate)}
  .sheet{position:relative;width:848px;height:1200px;overflow:hidden;background:var(--slate);
    font-family:"Encode Sans Semi Condensed",sans-serif;color:var(--white)}
  .deco{position:absolute;border-radius:50%;
    background:radial-gradient(circle at 40% 40%,var(--slate-light),rgba(90,101,103,.35) 70%,transparent 72%)}
  .deco--right{left:675px;top:-30px;width:260px;height:310px}
  .deco--left{left:20px;top:188px;width:150px;height:175px}
  .deco--bottom{left:-40px;top:790px;width:340px;height:400px}

  .wordmark{font-family:"Ubuntu",sans-serif;font-weight:500;letter-spacing:-1px;line-height:1;white-space:nowrap}
  .tagline{font-weight:400;line-height:1;white-space:nowrap}

  .hero{position:absolute;left:0;top:80px;width:848px;text-align:center}
  .hero .wordmark{font-size:100px}
  .hero .tagline{font-size:40px;margin-top:26px;letter-spacing:.5px}

  .pack{position:absolute;top:295px;width:303px;height:808px;box-shadow:4px 4px 6px rgba(0,0,0,.35)}
  .pack--front{left:103px;background:var(--white)}
  .pack--back{left:441px;background:var(--red)}

  .front-top{position:absolute;left:0;top:15px;width:303px;height:141px;background:var(--red);text-align:center;padding-top:28px}
  .front-top .wordmark{font-size:43px}
  .front-top .tagline{font-size:19px;margin-top:8px}
  .front-art{position:absolute;left:0;top:156px;width:303px;height:529px;
    background:linear-gradient(160deg,var(--pink) 0%,var(--white) 35%,var(--white) 55%,var(--sky) 75%,var(--pink) 100%)}
  .count{position:absolute;left:25px;top:632px;color:var(--red);font-weight:600;font-size:34px;line-height:1}
  .count small{font-size:25px;font-weight:500}
  .front-warning{position:absolute;left:0;top:685px;width:303px;height:109px;background:var(--red);padding:17px 20px 0 25px}
  .front-warning h3{font-weight:500;font-size:12.5px;display:flex;align-items:center;gap:6px}
  .front-warning p{font-size:7.6px;line-height:10px;margin-top:9px}

  .tear-line{position:absolute;left:0;top:37px;width:303px;height:10px}
  .back-brand{position:absolute;left:0;top:82px;width:303px;text-align:center}
  .back-brand .wordmark{font-size:47px}
  .back-brand .tagline{font-size:19px;margin-top:12px}
  .back-copy{position:absolute;left:38px;top:194px;width:226px;font-size:6.5px;line-height:8.5px;text-align:justify}
  .back-copy p+p{margin-top:8.5px}
  .allergy{position:absolute;left:40px;top:425px;width:224px;height:82px;border:2px solid var(--white);border-radius:5px;
    text-align:center;padding-top:12px}
  .allergy .lead{display:flex;align-items:center;justify-content:center;gap:8px;font-size:16px;font-weight:500}
  .allergy .lead span{display:block;text-align:left}
  .allergy .lead em{font-style:normal;font-size:12.5px;font-weight:400;display:block;margin-top:2px}
  .allergy .sub{font-size:12.5px;margin-top:2px}
  .symbols{position:absolute;left:118px;top:528px;display:flex;gap:12px;align-items:center}
  .symbols svg{display:block}
  .origin{position:absolute;left:38px;top:587px;font-size:10.5px;display:flex;gap:28px}
  .maker{position:absolute;left:38px;top:700px}
  .maker .name{font-family:"Ubuntu",sans-serif;font-weight:500;font-size:27px;line-height:1}
  .maker .web{font-size:14px;margin-top:8px}
  .maker .addr{font-size:10px;margin-top:6px}
</style>
</head>
<body>
<main class="sheet">
  <div class="deco deco--right" role="img" aria-label="Faint striped balloon decoration"></div>
  <div class="deco deco--left" role="img" aria-label="Faint striped balloon decoration"></div>
  <div class="deco deco--bottom" role="img" aria-label="Faint striped balloon decoration"></div>

  <header class="hero">
    <div class="wordmark">twirlpopix</div>
    <div class="tagline">high-quality latex balloons</div>
  </header>

  <section class="pack pack--front">
    <div class="front-top">
      <div class="wordmark">twirlpopix</div>
      <div class="tagline">high-quality latex balloons</div>
    </div>
    <div class="front-art" role="img" aria-label="Cluster of red, pink, light blue and striped balloons"></div>
    <div class="count">100 <small>PCS</small></div>
    <div class="front-warning">
      <h3>
        <svg width="20" height="18" viewBox="0 0 20 18" aria-hidden="true"><path d="M10 1 L19 17 H1 Z" fill="#fff"/><rect x="9" y="6" width="2" height="6" fill="#f5130f"/><rect x="9" y="13.5" width="2" height="2" fill="#f5130f"/></svg>
        WARNING : CHOKING HAZARD
      </h3>
      <p>Children under eight (8) years old can choke or suffocate on uninflated or broken balloons. Adult supervision is required. Keep uninflated balloons from reach of children. Discard broken balloons responsibly.</p>
    </div>
  </section>

  <section class="pack pack--back">
    <svg class="tear-line" viewBox="0 0 303 10" aria-hidden="true">
      <line x1="0" y1="5" x2="303" y2="5" stroke="#fff" stroke-width="1" stroke-dasharray="5 4"/>
      <g fill="none" stroke="#fff" stroke-width="1.2"><circle cx="252" cy="2" r="2"/><circle cx="252" cy="8" r="2"/><line x1="254" y1="3" x2="262" y2="8"/><line x1="254" y1="7" x2="262" y2="2"/></g>
    </svg>
    <div class="back-brand">
      <div class="wordmark">twirlpopix</div>
      <div class="tagline">high-quality latex balloons</div>
    </div>
    <div class="back-copy">
      <p>Our twisting balloons are made for artists, parents and party hosts who want bright shapes that hold. Each balloon is stretched, tested and packed by hand so it inflates evenly and twists without popping. Use a hand pump for best results, and leave a small tail at the end for tying. Keep balloons away from heat, sharp edges and direct sun to make your creations last longer at every event.</p>
      <p>Start with simple shapes such as dogs, swords and flowers, then move on to hats and larger sculptures. Inflate each balloon slowly and burp out a little air before you twist so the latex has room to move. Store unused balloons in a cool, dry place inside this bag and seal it after each use. Visit our website for free guides, color charts and new ideas from balloon artists around the world who share their favorite designs.</p>
    </div>
    <div class="allergy">
      <div class="lead">
        <svg width="34" height="30" viewBox="0 0 20 18" aria-hidden="true"><path d="M10 1 L19 17 H1 Z" fill="#fff"/><rect x="9" y="6" width="2" height="6" fill="#f5130f"/><rect x="9" y="13.5" width="2" height="2" fill="#f5130f"/></svg>
        <span>MADE OF 100%<em>Natural Rubber Latex</em></span>
      </div>
      <div class="sub">Which May Cause Allergic Reactions</div>
    </div>
    <div class="symbols">
      <svg width="28" height="28" viewBox="0 0 28 28" aria-hidden="true"><path d="M5 12 H15 L13.5 25 H6.5 Z" fill="#fff"/><circle cx="21" cy="5" r="2.5" fill="#fff"/><path d="M19 9 H23 V18 L24 26 H22 L21 19 L20 26 H18 L19 18 Z" fill="#fff"/></svg>
      <svg width="30" height="30" viewBox="0 0 30 30" aria-hidden="true"><circle cx="15" cy="15" r="13" fill="none" stroke="#fff" stroke-width="2"/><circle cx="15" cy="15" r="8" fill="none" stroke="#fff" stroke-width="1.5"/><line x1="6" y1="6" x2="24" y2="24" stroke="#fff" stroke-width="2"/></svg>
      <svg width="28" height="28" viewBox="0 0 28 28" aria-hidden="true"><path d="M14 3 L25 23 H3 Z" fill="none" stroke="#fff" stroke-width="3" stroke-dasharray="9 3"/></svg>
      <svg width="26" height="22" viewBox="0 0 26 22" aria-hidden="true"><rect x="1" y="1" width="24" height="20" rx="2" fill="#fff"/></svg>
    </div>
    <div class="origin"><span>Made In China</span><span>Net Wt. 25g</span></div>
    <div class="maker">
      <div class="name">TwirlPopics</div>
      <div class="web">www.twirlpopics.com</div>
      <div class="addr">Harborview, Maine</div>
    </div>
  </section>
</main>
</body>
</html>
```